Business Consultancy Wordpress Design

Small business analysis consultancy.

Looking for a bold, clean design for Wordpress. Final site will only be a few pages, some contact information, services provided and a little background information. Potentially a blog.

Colours to be as per logo, with either black or white as the main colour.

Link is www.halvicadvisory.com

More details to be included in the best few days

Name - Halvic Consulting
Provides - Project Consultancy
Updates

Project Deadline Extended
Reason: I am going to be on holiday with little access to the web over 28/02 - 05/03 and am therefore extending the deadline

Target Market(s)

Business professionals

Industry/Entity Type

Business

Colors

Designer to choose colors to be used in the design.

Requirements
Must have
• Must contain the logo in the header
Footer must fit a 3 column layout in wordpress

Business style, royalty free stock images
Nice to have
• Would like the 1 or 2 column wordpress style layout
Should not have
• must not be blog or magazine style layout or look and feel

```html
<!DOCTYPE html>
<html lang="en">
<head>
<meta charset="utf-8">
<title>Halvic Consulting</title>
<link href="https://fonts.googleapis.com/css2?family=Open+Sans:ital,wght@0,400;0,600;1,400;1,600&display=swap" rel="stylesheet">
<style>
:root{
  --blue:#1a8ad4;
  --green:#6aaa2a;
  --ink:#3a3a3a;
  --muted:#555;
  --grey-dark:#454545;
  --footer:#3d3d3d;
  --footer-bottom:#303030;
  --footer-text:#cfcfcf;
  --panel:#f0f0f0;
  --white:#fff;
}
*{box-sizing:border-box;margin:0;padding:0}
html,body{width:920px;height:1200px;overflow:hidden;background:var(--white)}
body{position:relative;font-family:'Open Sans',sans-serif;color:var(--ink)}
.abs{position:absolute}

.utility-nav{left:417px;top:14px;font-size:10px;letter-spacing:.2px;color:#444;display:flex;gap:12px;align-items:center}
.utility-nav span{display:flex;align-items:center;gap:5px}
.search{left:693px;top:9px;width:152px;height:24px;border:1px solid #ddd;border-radius:3px;background:#fafafa}
.search svg{position:absolute;right:7px;top:4px}

.brand{left:77px;top:32px;display:flex;align-items:center;gap:10px}
.brand-dot{width:28px;height:28px;border-radius:50%;background:var(--blue)}
.brand-name{font-size:19px;color:#555;letter-spacing:.3px}

.main-nav{left:346px;top:70px;width:574px;height:32px;background:var(--blue);clip-path:polygon(30px 0,100% 0,100% 100%,0 100%)}
.main-nav ul{list-style:none;display:flex;gap:16px;position:absolute;left:53px;top:8px;font-size:11.5px;color:var(--white)}
.main-nav li.active{font-weight:600}
.accent-line{left:0;top:97px;width:349px;height:5px;background:var(--green)}

.hero{left:0;top:102px;width:920px;height:340px;background:linear-gradient(180deg,#2e5fb0 0%,#7fa6d8 35%,#c9d9ec 55%,#4f8a2a 72%,#2f6a18 100%)}
.hero-dots{left:421px;top:411px;display:flex;gap:10px}
.hero-dots i{width:9px;height:9px;border-radius:50%;background:#ddd;display:block}
.hero-dots i.on{width:12px;height:12px;margin-top:-1.5px;background:var(--blue)}

.feature{top:476px;width:180px;text-align:center}
.feature .circle{width:92px;height:92px;border-radius:50%;background:var(--blue);margin:0 auto;display:flex;align-items:center;justify-content:center}
.feature .circle.dark{background:var(--grey-dark)}
.feature h3{margin-top:20px;font-size:18px;font-weight:400;color:var(--green)}

.welcome{left:77px;top:632px;width:600px}
.welcome h2{font-size:19px;font-weight:400;color:#333}
.welcome h2 em{font-style:normal;color:var(--blue)}
.welcome p{margin-top:18px;font-size:10px;font-style:italic;line-height:14px;color:#333}
.welcome p+p{margin-top:14px}
.welcome-art{left:692px;top:628px;width:140px;height:148px;background:linear-gradient(135deg,#ffd82a 0%,#f0492c 40%,#9a4fd0 65%,#2f8ae6 100%);border-radius:4px;opacity:.9}

.footer{left:0;top:926px;width:920px;height:216px;background:var(--footer)}
.footer-bottom{left:0;top:1142px;width:920px;height:58px;background:var(--footer-bottom)}

.blog{left:100px;top:802px;width:720px;height:165px;background:var(--panel);border:1px solid #ddd;box-shadow:0 1px 4px rgba(0,0,0,.2)}
.blog h2{position:absolute;left:15px;top:12px;font-size:19px;font-weight:400;color:#333}
.blog h2 em{font-style:normal;color:var(--blue)}
.blog-arrows{position:absolute;right:19px;top:22px;display:flex;gap:3px}
.blog-post{position:absolute;top:55px;width:230px}
.blog-post .thumb{position:absolute;left:0;top:0;width:45px;height:45px;border:2px solid #fff;box-shadow:0 0 2px rgba(0,0,0,.3);background:linear-gradient(135deg,#d9d9d9,#8a8a8a)}
.blog-post .text{position:absolute;left:60px;top:0;width:170px;font-style:italic}
.blog-post h4{font-size:10px;font-weight:600;color:var(--blue)}
.blog-post p{margin-top:3px;font-size:9.5px;line-height:15.5px;color:#444}
.blog-post small{display:block;margin-top:11px;font-size:8.5px;color:var(--green)}

.foot-col{top:995px;width:190px}
.foot-col h5{font-size:12.5px;font-weight:400;color:var(--green)}
.foot-col ul{list-style:none;margin-top:6px}
.foot-col li{font-size:9px;line-height:21.6px;color:var(--footer-text);padding-left:15px;position:relative}
.foot-col li::before{content:"";position:absolute;left:1px;top:10px;width:5px;height:1px;background:var(--blue)}
.foot-col li::after{content:"";position:absolute;left:4px;top:8.5px;border-left:3px solid var(--blue);border-top:2px solid transparent;border-bottom:2px solid transparent}

.newsletter-input{left:675px;top:1027px;width:169px;height:28px;background:#6a6a6a;border-radius:2px;font-size:9.5px;font-style:italic;color:#ddd;padding:7px 10px}
.subscribe{left:774px;top:1069px;width:70px;height:25px;background:var(--blue);color:var(--white);font-size:8.5px;font-weight:600;letter-spacing:.5px;text-align:center;line-height:25px}
.connect{left:674px;top:1108px;font-size:13px;color:var(--green)}
.social{top:1105px;width:28px;height:28px;border-radius:50%;background:#1e1e1e}

.foot-brand{left:77px;top:1155px;display:flex;align-items:center;gap:10px}
.foot-brand .brand-dot{width:34px;height:34px}
.copyright{font-size:8.5px;color:#888}
.copyright b{font-weight:400;color:#bbb}
.legal{right:100px;top:1167px;font-size:8.5px;color:#888}
</style>
</head>
<body>

<nav class="utility-nav abs"><span>CAREERS</span><span>INVESTORS</span><span>CONTACT US</span><span>WORLDWIDE
  <svg width="13" height="13" viewBox="0 0 13 13"><circle cx="6.5" cy="6.5" r="5.5" fill="none" stroke="#444" stroke-width="1.4"/><path d="M3 4c2 0 2 2 4 2s1 3 0 4M8 2c0 2 2 2 3 3" fill="none" stroke="#444" stroke-width="1.2"/></svg></span></nav>
<div class="search abs"><svg width="15" height="15" viewBox="0 0 15 15"><circle cx="6" cy="6" r="4.3" fill="none" stroke="#4c9a2a" stroke-width="2"/><line x1="9.2" y1="9.2" x2="13.5" y2="13.5" stroke="#4c9a2a" stroke-width="2.6" stroke-linecap="round"/></svg></div>

<header class="brand abs"><div class="brand-dot"></div><div class="brand-name">HALVIC CONSULTING</div></header>

<nav class="main-nav abs"><ul>
  <li class="active">HOME</li><li>ABOUT US</li><li>SERVICES</li><li>GALLERY</li><li>BLOG</li><li>TESTIMONIALS</li><li>CONTACT US</li>
</ul></nav>
<div class="accent-line abs"></div>

<section class="hero abs" role="img" aria-label="Business people in suits standing in a green field under a blue sky, each holding a lightbulb sign over their head"></section>
<div class="hero-dots abs"><i class="on"></i><i></i><i></i><i></i></div>

<div class="feature abs" style="left:76px">
  <div class="circle dark"><svg width="38" height="44" viewBox="0 0 38 44"><rect x="2" y="2" width="34" height="40" rx="2" fill="none" stroke="#fff" stroke-width="3"/><rect x="7" y="7" width="24" height="30" fill="#fff"/><circle cx="19" cy="15" r="3.5" fill="#454545"/><rect x="12" y="21" width="14" height="3" fill="#454545"/><rect x="10" y="27" width="18" height="2" fill="#454545"/><rect x="10" y="31" width="18" height="2" fill="#454545"/></svg></div>
  <h3>Business Strategy</h3>
</div>
<div class="feature abs" style="left:272px">
  <div class="circle"><svg width="56" height="50" viewBox="0 0 56 50"><circle cx="38" cy="14" r="11" fill="none" stroke="#fff" stroke-width="2.5"/><path d="M27 14h22M38 3v22M30 7c5 3 11 3 16 0M30 21c5-3 11-3 16 0" fill="none" stroke="#fff" stroke-width="1.6"/><path d="M6 30c2-9 9-14 17-13l-2-5 9 7-9 6 1-4c-6 0-11 4-12 9z" fill="#fff"/><path d="M44 30c-2 9-10 14-18 13l2 5-9-7 9-6-1 4c6 0 11-4 13-9z" fill="#fff"/></svg></div>
  <h3>Project Management</h3>
</div>
<div class="feature abs" style="left:464px">
  <div class="circle"><svg width="44" height="40" viewBox="0 0 44 40"><rect x="4" y="2" width="8" height="34" fill="#fff"/><rect x="15" y="14" width="8" height="22" fill="#fff"/><rect x="26" y="22" width="8" height="14" fill="#fff"/><rect x="1" y="37" width="42" height="2" fill="#fff"/></svg></div>
  <h3>Services</h3>
</div>
<div class="feature abs" style="left:667px">
  <div class="circle"><svg width="46" height="46" viewBox="0 0 46 46"><path d="M9 24a14 14 0 0 1 28 0" fill="none" stroke="#fff" stroke-width="4"/><rect x="5" y="22" width="8" height="13" rx="3" fill="#fff"/><rect x="33" y="22" width="8" height="13" rx="3" fill="#fff"/><path d="M37 35c0 5-6 7-12 7" fill="none" stroke="#fff" stroke-width="2.5"/><circle cx="24" cy="42" r="2.5" fill="#fff"/></svg></div>
  <h3>Customer Support</h3>
</div>

<section class="welcome abs">
  <h2>Welcome to <em>Halvic Consulting</em></h2>
  <p>Our business is centered around helping online and mobile companies (usually gaming companies, ad serving companies) utilize their data to help them grow and optimize their businesses. We believe in understanding data to uncover clues that optimize and grow businesses. With a background in big data, gaming, and media, we provide a unique blend of technical, statistical, and business expertise.</p>
  <p>We specialize in statistical analysis and visualization of data to help make sense of vast amounts of information... we find patterns and insights which highlight opportunities for our clients to attract more users, serve better ads, develop better product features... in short, we grow businesses with data.</p>
</section>
<div class="welcome-art abs" role="img" aria-label="Illustration of silhouetted business people building a staircase of colourful blocks"></div>

<div class="footer abs"></div>

<section class="blog abs">
  <h2>Blog <em>Posts</em></h2>
  <div class="blog-arrows">
    <svg width="13" height="13" viewBox="0 0 13 13"><circle cx="6.5" cy="6.5" r="6.5" fill="#aaa"/><path d="M7.5 3.5 4.5 6.5l3 3" fill="none" stroke="#fff" stroke-width="1.6"/></svg>
    <svg width="13" height="13" viewBox="0 0 13 13"><circle cx="6.5" cy="6.5" r="6.5" fill="#222"/><path d="M5.5 3.5l3 3-3 3" fill="none" stroke="#fff" stroke-width="1.6"/></svg>
  </div>
  <article class="blog-post" style="left:17px">
    <div class="thumb" role="img" aria-label="Photo of a hand signing a document"></div>
    <div class="text"><h4>Aliquam molestie</h4><p>Mi et imperdiet euismod, dui purus auctor tellus, et interdum lacus lectus et ante...</p><small>Posted on 3 days ago</small></div>
  </article>
  <article class="blog-post" style="left:260px">
    <div class="thumb" role="img" aria-label="Photo of hands working on paperwork"></div>
    <div class="text"><h4>Aliquam molestie</h4><p>Mi et imperdiet euismod, dui purus auctor tellus, et interdum lacus lectus et ante...</p><small>Posted on 3 days ago</small></div>
  </article>
  <article class="blog-post" style="left:498px">
    <div class="thumb" role="img" aria-label="Photo of a business handshake over documents"></div>
    <div class="text"><h4>Aliquam molestie</h4><p>Mi et imperdiet euismod, dui purus auctor tellus, et interdum lacus lectus et ante...</p><small>Posted on 3 days ago</small></div>
  </article>
</section>

<div class="foot-col abs" style="left:77px"><h5>Footer Navigation</h5><ul><li>Sed ut perspiciatis unde omnis</li><li>Iste natus error sit voluptatem</li><li>Accusantium dolorem</li><li>Que laudantium</li><li>Totam rem aperiam.</li></ul></div>
<div class="foot-col abs" style="left:279px"><h5>Footer Navigation</h5><ul><li>Sed ut perspiciatis unde omnis</li><li>Iste natus error sit voluptatem</li><li>Accusantium dolorem</li><li>Que laudantium</li><li>Totam rem aperiam.</li></ul></div>
<div class="foot-col abs" style="left:478px"><h5>Footer Navigation</h5><ul><li>Sed ut perspiciatis unde omnis</li><li>Iste natus error sit voluptatem</li><li>Accusantium dolorem</li><li>Que laudantium</li><li>Totam rem aperiam.</li></ul></div>
<div class="foot-col abs" style="left:674px"><h5>Newsletter Subscribe</h5></div>
<div class="newsletter-input abs">Enter Email Address</div>
<div class="subscribe abs">SUBSCRIBE</div>
<div class="connect abs">Connect</div>
<div class="social abs" style="left:739px"></div>
<div class="social abs" style="left:777px"></div>
<div class="social abs" style="left:816px"></div>

<div class="footer-bottom abs"></div>
<div class="foot-brand abs"><div class="brand-dot"></div><div class="copyright">Copyright © 2014 . <b>Halvic Consulting</b>. All Right Reserved</div></div>
<div class="legal abs">Privacy Policy &nbsp;|&nbsp; Term of Services &nbsp;|&nbsp; FAQ &nbsp;|&nbsp; Site Map</div>

</body>
</html>
```